Roadside building business signage for a holistic health clinic.

Replace signs as shown in the attached file. They are perforated stickers that go on the windows as shown. Looking for something that has our logo and says the name of the practice with logo (Fernbrook Health & Wellness) also boldly says Acupuncture, IV Vitamins, and Holistic Health.
Possibly our phone number as well 318-627-5194
Updates

Please don't use pink except the logo. Earthy, organic tone colors appreciated.

Need of eye catching window signage of a holistic clinic on a brick building. Pink, purple, sage green, white color. Logo is pink on a white background. Please don't overload with too much pink. Words to include are "Fernbrook Health and Wellness(name of business)", "Direct Primary Care", " Medical acupuncture", "IV Vitamin Therapy", "fernbrookcare-example.com","318-627-5194".

Target Market(s)

People will see in their cars passing by the building. Busy roadside so need to be visible while passing in fast speed.

Industry/Entity Type

Health & Wellness

Font styles to use
Sans Serif

Colors

Designer to choose colors to be used in the design.

Requirements
Must have
• On sign must have words Holistic Medicine, Medical Acupuncture, Direct Primary Care and IV vitamins.
Nice to have
• Simple, minimalistic, artistic yet has clear message. White, Black, Violet, Pink (logo), Dark green, Sage green.
Should not have
• Bold colors (red, yellow, blue), same tone colors. Blue waves on the current signage (uploaded file) must go.

```html
<!DOCTYPE html>
<html lang="en">
<head>
<meta charset="utf-8">
<title>Fernbrook Health &amp; Wellness — Window Signage</title>
<link href="https://fonts.googleapis.com/css2?family=Red+Hat+Display:wght@600;700&display=swap" rel="stylesheet">
<style>
  :root {
    --backdrop: #d1d1d1;
    --panel-white: #ffffff;
    --forest: #0e4a3f;
    --sage-top: #7f9c7b;
    --sage-bottom: #5f7f5c;
    --brand-pink: #df4f8e;
    --text-light: #ffffff;
    --shadow: rgba(0, 0, 0, 0.35);
  }
  * { box-sizing: border-box; margin: 0; padding: 0; }
  html, body {
    width: 818px;
    height: 1200px;
    overflow: hidden;
    background: var(--backdrop);
  }
  .canvas {
    position: relative;
    width: 818px;
    height: 1200px;
    font-family: "Red Hat Display", sans-serif;
  }
  .sign-row {
    position: absolute;
    left: 119px;
    display: flex;
    gap: 44px;
  }
  .sign-row--forest { top: 45px; }
  .sign-row--sage { top: 374px; }

  .panel {
    width: 268px;
    height: 268px;
    box-shadow: 6px 7px 8px var(--shadow);
  }
  .panel--logo {
    background: var(--panel-white);
    display: flex;
    flex-direction: column;
    align-items: center;
    justify-content: center;
    gap: 10px;
  }
  .brand-dot {
    width: 44px;
    height: 44px;
    border-radius: 50%;
    background: var(--brand-pink);
  }
  .brand-name {
    color: var(--forest);
    font-weight: 600;
    text-align: center;
    line-height: 1.15;
  }
  .brand-name__main {
    display: block;
    font-size: 30px;
    letter-spacing: 1px;
  }
  .brand-name__sub {
    display: block;
    font-size: 10px;
    letter-spacing: 2px;
    text-transform: uppercase;
  }

  .panel--message {
    padding: 24px 20px 0 22px;
    color: var(--text-light);
    font-weight: 700;
  }
  .panel--forest { background: var(--forest); }
  .panel--sage {
    background: linear-gradient(180deg, var(--sage-top), var(--sage-bottom));
  }
  .services {
    font-size: 20px;
    line-height: 30px;
    white-space: nowrap;
  }
  .phone {
    margin-top: 22px;
    font-size: 24px;
    font-weight: 700;
    letter-spacing: 0.3px;
  }
  .website {
    margin-top: 6px;
    font-size: 15px;
    font-weight: 600;
    white-space: nowrap;
  }
</style>
</head>
<body>
  <main class="canvas">
    <section class="sign-row sign-row--forest">
      <div class="panel panel--logo">
        <span class="brand-dot" aria-hidden="true"></span>
        <p class="brand-name">
          <span class="brand-name__main">Fernbrook</span>
          <span class="brand-name__sub">Health &amp; Wellness</span>
        </p>
      </div>
      <div class="panel panel--message panel--forest">
        <p class="services">Direct Primary Care<br>Medical Acupuncture<br>IV Vitamins<br>Holistic Medicine</p>
        <p class="phone">318-627-5194</p>
        <p class="website">fernbrookcare-example.com</p>
      </div>
    </section>

    <section class="sign-row sign-row--sage">
      <div class="panel panel--logo">
        <span class="brand-dot" aria-hidden="true"></span>
        <p class="brand-name">
          <span class="brand-name__main">Fernbrook</span>
          <span class="brand-name__sub">Health &amp; Wellness</span>
        </p>
      </div>
      <div class="panel panel--message panel--sage">
        <p class="services">Direct Primary Care<br>Medical Acupuncture<br>IV Vitamins<br>Holistic Medicine</p>
        <p class="phone">318-627-5194</p>
        <p class="website">fernbrookcare-example.com</p>
      </div>
    </section>
  </main>
</body>
</html>
```